I am writing a book called "SMILING OPENS EVERY DOOR "

I NEED A BOOK COVER FOR MY BOOK" SMILING OPENS EVERY DOOR"
So who knocked on it first? " ( this in smaller font)

"Smiling Opens Every Door " will need to designed to eventually be a logo , banner and business card
COLOURS MAINLY ORANGE AND WHITE (with accents bright colour )

THE BOOK IS MY LAUGHTER JOURNEY AS A PERFORMER AND ADVENTURE INDIA LEARNING ABOUT LAUGHTER YOGA WHICH I WILL BE TEACHING

I do not want photos on the front cover ..
The look could be modern and eye-catching
I have also just been to India to learn Laughing Yoga with Dr Tobin Verhaal

Thank-you so much everyone for your brilliant designs . i am overwhelmed with your talent . i hope to work with you all again soon ! Marnie  

Target Market(s)

"Adults based in western speaking countries aged 25 to 60 that want to learn to laugh more
Also this book will be sold at my conference workshops

Industry/Entity Type

Business

Requirements
Must have
• ORANGE AND WHITE
CAN HAVE AQUA , HOT PINK , LIME GREEN, YELLOW ACCENTS

THESE WILL BE DIFFERENT AREAS WILL COVERING IN MY BOOK
EG LAUGHTER NAD BREAT CANCER ( PINK)
LAUGHTER NAD DEPRESSION ( BLUE)
SMILES AND LITTLE ONES ( YELLOW)

NO Photos on front cover
Should not have
• No photos

```html
<!DOCTYPE html>
<html lang="en">
<head>
<meta charset="utf-8">
<title>Smiling Opens Every Door – Book Cover</title>
<link rel="stylesheet" href="https://fonts.googleapis.com/css2?family=Arimo:wght@400&family=Kaushan+Script&family=Open+Sans:wght@700&display=swap">
<style>
  :root {
    --orange-light: #f7941d;
    --orange-mid: #f15a24;
    --orange-deep: #ee4f23;
    --ornament: rgba(255, 160, 60, 0.35);
    --lotus: rgba(230, 70, 30, 0.55);
    --white: #ffffff;
    --yellow-text: #ffe11a;
    --band-yellow: #ffe21c;
    --band-red: #e5382b;
  }
  html, body {
    margin: 0;
    padding: 0;
    overflow: hidden;
    background: #ffffff;
  }
  .cover {
    position: relative;
    width: 799px;
    height: 1200px;
    overflow: hidden;
    background: linear-gradient(180deg,
      var(--orange-light) 0%,
      var(--orange-mid) 30%,
      var(--orange-deep) 55%,
      var(--orange-light) 88%);
    font-family: "Open Sans", sans-serif;
  }
  .top-ornament {
    position: absolute;
    left: 210px;
    top: -190px;
    width: 380px;
    height: 380px;
    border-radius: 50%;
    background: radial-gradient(circle, var(--ornament) 0%, rgba(255,160,60,0.15) 70%, rgba(255,160,60,0) 100%);
  }
  .author {
    position: absolute;
    top: 48px;
    left: 0;
    width: 100%;
    margin: 0;
    text-align: center;
    color: var(--white);
    font-size: 52px;
    font-weight: 700;
    letter-spacing: 0.5px;
  }
  .title {
    position: absolute;
    top: 290px;
    left: 0;
    width: 100%;
    margin: 0;
    text-align: center;
    color: var(--white);
    font-family: "Kaushan Script", cursive;
    font-weight: 400;
    text-shadow: 4px 6px 6px rgba(110, 30, 10, 0.55);
    line-height: 1;
  }
  .title-main {
    display: block;
    font-size: 156px;
  }
  .title-second {
    display: block;
    margin-top: -4px;
  }
  .title-small {
    font-family: "Open Sans", sans-serif;
    font-weight: 700;
    font-size: 48px;
    margin-right: 12px;
  }
  .title-large {
    font-size: 136px;
  }
  .tagline {
    position: absolute;
    top: 672px;
    left: 0;
    width: 100%;
    margin: 0;
    text-align: center;
    color: var(--yellow-text);
    font-size: 44px;
    font-weight: 700;
  }
  .lotus {
    position: absolute;
    left: 160px;
    top: 740px;
    width: 480px;
    height: 300px;
  }
  .series-band {
    position: absolute;
    left: 0;
    bottom: 0;
    width: 100%;
    height: 140px;
    background: var(--band-yellow);
    display: flex;
    align-items: center;
    justify-content: center;
  }
  .series-label {
    margin: 0;
    color: var(--band-red);
    font-family: "Arimo", sans-serif;
    font-size: 58px;
    font-weight: 400;
  }
</style>
</head>
<body>
  <main class="cover">
    <div class="top-ornament" role="img" aria-label="Faint circular mandala ornament"></div>

    <p class="author">Marnie Hollins</p>

    <h1 class="title">
      <span class="title-main">Smiling</span>
      <span class="title-second"><span class="title-small">opens every</span><span class="title-large">Door</span></span>
    </h1>

    <p class="tagline">So who knocked on it first?</p>

    <svg class="lotus" viewBox="0 0 480 300" role="img" aria-label="Soft lotus flower ornament">
      <path d="M10 230 Q120 140 170 80 Q240 -10 310 80 Q360 140 470 230 Q360 300 240 300 Q120 300 10 230 Z" fill="var(--lotus)"/>
    </svg>

    <div class="series-band">
      <p class="series-label">SMILES and LITTLE ONES</p>
    </div>
  </main>
</body>
</html>
```